Vexel Business Cards

We need a new look business cvard to refelect our new look website www.vexel-example.com.au
We’re Vexel, a team of town planning and traffic and transport engineering specialists located in Melbourne.

Vexel is a company that is structured, articulate, dynamic, progressive, accurate and adaptable.
Our key messages are:
1. We make your life easier by doing what we do best
2. We tell you what you need to know not what you want to hear
3. Polished and professional but not afraid to show some personality

we would like a bold new look that is polished and professional but not afraid to show a bit of personality

Target Market(s)

Vexel’s diverse client base consists of architecture practices, builders, developers, local government and the legal fraternity.

Industry/Entity Type

Town

Requirements
Must have
• must use our logo and have the following information

Joel Harcastle
Director

Vexel Consultants Pty Ltd
Fernhollow first floor
Tamber Street
Ashbrook VIC 3188 Australia
+61 03 9555 0187
mail@vexel-example.com.au
www.vexel-example.com.au
Nice to have
• We would like to see the logo used or the colours of the logo used.

```html
<!DOCTYPE html>
<html lang="en">
<head>
<meta charset="utf-8">
<title>Vexel Business Cards</title>
<link rel="stylesheet" href="https://fonts.googleapis.com/css2?family=Source+Sans+3:wght@400;600;700&display=swap">
<style>
  :root {
    --stage: #151515;
    --card: #e6e7e8;
    --dot: #c4c6c8;
    --ink: #3d4650;
    --text: #5a636b;
    --accent: #1ba1dc;
    --tile-blue: #2a9bd8;
    --tile-green: #3d9a52;
  }
  * { box-sizing: border-box; margin: 0; padding: 0; }
  html, body {
    width: 1200px; height: 844px; overflow: hidden;
    background: var(--stage);
    font-family: "Source Sans 3", "Myriad Pro", sans-serif;
  }
  .card {
    position: absolute;
    top: 309px;
    width: 365px; height: 224px;
    background-color: var(--card);
    background-image: radial-gradient(circle, var(--dot) 0.8px, transparent 1.2px);
    background-size: 25px 25px;
    background-position: 10px 12px;
    overflow: hidden;
  }
  .card--front { left: 217px; }
  .card--back { left: 611px; }

  .web-address {
    position: absolute; right: 207px; top: 115px;
    font-size: 10px; color: var(--text); white-space: nowrap;
  }
  .tile { position: absolute; }
  .tile--building-a { left: 166px; top: 75px; width: 49px; height: 49px; background: linear-gradient(160deg, #4db8ea, var(--tile-blue)); }
  .tile--building-b { left: 266px; top: 75px; width: 49px; height: 49px; background: linear-gradient(160deg, #6cc07a, var(--tile-green)); }
  .tile--signage    { left: 216px; top: 125px; width: 49px; height: 49px; background: linear-gradient(160deg, #74bd6a, #3f8d4a); }
  .tile--tower      { left: 316px; top: 125px; width: 49px; height: 49px; background: linear-gradient(160deg, #55c0ee, #1f86c4); }
  .tile--drafting   { left: 67px; top: 178px; width: 98px; height: 46px; background: linear-gradient(150deg, #c9c9c9, #7f7f7f); }
  .tile--water      { left: 168px; top: 178px; width: 97px; height: 46px; background: linear-gradient(150deg, #3fa8e0, #1666a8); }
  .tile--leaves     { left: 268px; top: 178px; width: 97px; height: 46px; background: linear-gradient(150deg, #6cc060, #2d7a34); }

  .brand-name {
    position: absolute; left: 26px; top: 136px;
    font-size: 38px; font-weight: 400; color: #4a5560; letter-spacing: 0.5px;
  }
  .contact { position: absolute; left: 212px; top: 45px; }
  .contact__name { font-size: 15px; font-weight: 700; color: var(--ink); line-height: 18px; }
  .contact__role { font-size: 13.5px; font-weight: 700; color: var(--accent); line-height: 18px; }
  .contact__address {
    margin-top: 22px; font-size: 10px; color: var(--text); line-height: 13px; font-style: normal;
  }
  .contact__lines { margin-top: 4px; font-size: 10px; color: var(--text); line-height: 13.5px; }
  .contact__label { color: var(--accent); font-weight: 700; display: inline-block; width: 12px; }
</style>
</head>
<body>
  <section class="card card--front" aria-label="Card front">
    <p class="web-address">www.vexel-example.com.au</p>
    <div class="tile tile--building-a" role="img" aria-label="Photo of apartment building in blue tone"></div>
    <div class="tile tile--building-b" role="img" aria-label="Photo of building in green tone"></div>
    <div class="tile tile--signage" role="img" aria-label="Photo of building signage in green tone"></div>
    <div class="tile tile--tower" role="img" aria-label="Photo of office tower in blue tone"></div>
    <div class="tile tile--drafting" role="img" aria-label="Black and white photo of plans being drafted"></div>
    <div class="tile tile--water" role="img" aria-label="Photo of blue water"></div>
    <div class="tile tile--leaves" role="img" aria-label="Photo of green leaves"></div>
  </section>

  <section class="card card--back" aria-label="Card back">
    <p class="brand-name">vexel</p>
    <div class="contact">
      <p class="contact__name">Joel Harcastle</p>
      <p class="contact__role">Director</p>
      <address class="contact__address">
        Vexel Consultants Pty Ltd<br>
        Fernhollow first floor<br>
        Tamber Street<br>
        Ashbrook VIC 3188 Australia
      </address>
      <p class="contact__lines">
        <span class="contact__label">P</span> +61 03 9555 0187<br>
        <span class="contact__label">E</span> mail@vexel-example.com.au
      </p>
    </div>
  </section>
</body>
</html>
```